Brick nest business card for client

Require a business card design for a new company based in Trinidad & Tobago called "Brick nest".

We source building supplies for resident and commercial projects. We manage and supply all your building solutions.

Exp: If you was to build a house or commercial building, My company Brick nest will supply and install all your building needs. Floor tile, Windows, Door, Molding .

Target Market(s)

Construction client

Industry/Entity Type

Building

Contact Information for Business Card

BRICK NEST LIMITED
VERDANT TRADE COURT
LA PALMERA, EXT. NO. 4, BLDG 3
SAN JUAN, TRINIDAD, W.I.
868-642-9087
bricknestlimited.example
derek@bricknestlimited.example

Font styles to use
Serif

Requirements
Must have
• Company name
• Address
• My Name: Derek Rampersook
• Director
Nice to have
• Modern business card (With a new logo)

```html
<!DOCTYPE html>
<html lang="en">
<head>
<meta charset="utf-8">
<title>Brick Nest Limited – Business Card</title>
<link rel="stylesheet" href="https://fonts.googleapis.com/css2?family=Marcellus&display=swap">
<style>
  :root {
    --backdrop: #e9e6e1;
    --card: #fbfbfa;
    --ink: #1d1d1d;
    --ink-soft: #333333;
    --skyline-light: #d3d7da;
    --skyline: #a9afb3;
    --band: #9fa6ab;
    --accent: #e0b96b;
  }
  * { margin: 0; padding: 0; box-sizing: border-box; }
  html, body {
    width: 1200px;
    height: 901px;
    overflow: hidden;
    background: var(--backdrop);
    font-family: "Marcellus", serif;
    color: var(--ink);
  }
  .business-card {
    position: absolute;
    left: 100px;
    top: 165px;
    width: 1000px;
    height: 572px;
    background: var(--card);
    box-shadow: 0 10px 30px rgba(0,0,0,0.18);
    overflow: hidden;
  }
  .address {
    position: absolute;
    left: 70px;
    top: 52px;
    font-size: 25px;
    line-height: 1.3;
    color: var(--ink-soft);
  }
  .brand {
    position: absolute;
    right: 70px;
    top: 120px;
    text-align: right;
  }
  .brand-name {
    display: flex;
    align-items: center;
    justify-content: flex-end;
    gap: 16px;
    font-size: 62px;
    line-height: 1;
    color: var(--ink);
  }
  .brand-mark {
    width: 26px;
    height: 26px;
    background: var(--accent);
  }
  .brand-suffix {
    margin-top: 8px;
    font-size: 18px;
    letter-spacing: 0.6em;
    margin-right: -0.6em;
    color: var(--ink);
  }
  .tagline {
    margin-top: 6px;
    font-size: 17px;
    color: var(--ink-soft);
  }
  .employee {
    position: absolute;
    right: 70px;
    top: 300px;
    text-align: right;
  }
  .employee-name { font-size: 36px; line-height: 1.1; }
  .employee-title { font-size: 26px; color: var(--ink-soft); margin-top: 4px; }
  .skyline {
    position: absolute;
    left: 0;
    right: 0;
    top: 330px;
    bottom: 74px;
    background: linear-gradient(to bottom, rgba(211,215,218,0) 0%, var(--skyline-light) 35%, var(--skyline) 100%);
  }
  .contact-band {
    position: absolute;
    left: 0;
    right: 0;
    bottom: 0;
    height: 74px;
    background: var(--band);
    display: flex;
    align-items: center;
    justify-content: center;
    gap: 22px;
    font-size: 23px;
    color: var(--ink);
  }
  .divider { color: var(--ink-soft); }
</style>
</head>
<body>
  <article class="business-card">
    <p class="address">
      Verdant Trade Court<br>
      La Palmera, Ext. No. 4, Bldg 3<br>
      San Juan, Trinidad, W.I.
    </p>

    <div class="brand">
      <div class="brand-name"><span class="brand-mark"></span>Brick Nest</div>
      <div class="brand-suffix">LIMITED</div>
      <div class="tagline">For All Your Building Solutions...</div>
    </div>

    <div class="employee">
      <div class="employee-name">Derek Rampersook</div>
      <div class="employee-title">Director</div>
    </div>

    <div class="skyline" role="img" aria-label="Grey city skyline illustration of office towers and buildings"></div>

    <div class="contact-band">
      <span class="phone">868-642-9087</span>
      <span class="divider">|</span>
      <span class="email">derek@bricknestlimited.example</span>
      <span class="divider">|</span>
      <span class="web">www.bricknestlimited.example</span>
    </div>
  </article>
</body>
</html>
```